Need a new letterhead

Need a new fresh exciting letterhead. Remove the footer...info is outdated.

Target Market(s)

B2B

Industry/Entity Type

Electrical Power

Colors

Designer to choose colors to be used in the design.

Requirements
Must have
• Red and Blue Corvane Systems Logo
Nice to have
• Lighting the way to sustainability in footer...reorganize the words?

```html
<!DOCTYPE html>
<html lang="en">
<head>
<meta charset="utf-8">
<title>Corvane Systems Letterhead</title>
<link href="https://fonts.googleapis.com/css2?family=Open+Sans:wght@400;700&family=Roboto:wght@400&display=swap" rel="stylesheet">
<style>
  :root{
    --brand-red:#e3121b;
    --brand-blue:#1f2a78;
    --ink:#4a4a4a;
    --ink-dark:#2a2a2a;
    --paper:#f7f7f7;
    --backdrop:#d4d4d4;
    --badge-line:#777;
    --badge-fill:#efefef;
  }
  *{margin:0;padding:0;box-sizing:border-box}
  html,body{width:1200px;height:1108px;overflow:hidden;background:var(--backdrop)}
  .letterhead{
    position:absolute;left:226px;top:24px;width:747px;height:1060px;
    background:var(--paper);overflow:hidden;
    font-family:"Open Sans",Arial,sans-serif;color:var(--ink);
  }
  .brand{
    position:absolute;left:55px;top:86px;
    display:flex;align-items:center;gap:10px;
  }
  .brand-mark{width:22px;height:22px;background:var(--brand-blue)}
  .brand-name{
    font-family:"Open Sans",Arial,sans-serif;font-weight:700;
    font-size:30px;color:var(--brand-red);letter-spacing:-0.3px;
  }
  .contact{
    position:absolute;left:474px;top:54px;
    font-family:"Roboto",Arial,sans-serif;font-size:12.6px;line-height:16.5px;color:var(--ink-dark);
    list-style:none;
  }
  .contact li{display:flex;align-items:center;gap:5px}
  .contact .address{display:block;margin-bottom:2px;line-height:16px}
  .contact svg{width:11px;height:11px;flex:none}
  .letter-body{
    position:absolute;left:62px;top:215px;width:623px;
    font-size:14.2px;line-height:20.9px;
  }
  .salutation{margin-bottom:21px}
  .letter-body p.copy{text-align:justify;margin-bottom:20.8px}
  .signature{
    position:absolute;left:62px;top:760px;width:90px;height:88px;
    background:linear-gradient(135deg,#ececec,#e2e2e2);
  }
  .partner-badge{
    position:absolute;left:58px;top:873px;width:210px;height:87px;
    border:1px solid var(--badge-line);background:var(--badge-fill);
  }
  .footer-wave{position:absolute;left:0;top:959px;width:747px;height:101px}
  .footer-web{
    position:absolute;left:55px;top:1019px;
    display:flex;align-items:center;gap:6px;
    font-family:"Roboto",Arial,sans-serif;font-size:14px;color:#fff;
  }
  .footer-web svg{width:12px;height:12px}
</style>
</head>
<body>
<main class="letterhead">
  <header>
    <div class="brand">
      <span class="brand-mark"></span>
      <span class="brand-name">Corvane Systems</span>
    </div>
    <ul class="contact">
      <li class="address">417 Harlow Street Brenton,<br>Maryland 21400</li>
      <li><svg viewBox="0 0 12 12"><path d="M2.5 1l2 2.3-1.2 1.4a7 7 0 0 0 4 4l1.4-1.2 2.3 2-1.3 1.5C5 10.7 1.3 7 .9 2.3z" fill="var(--brand-red)"/></svg>555-310-4820</li>
      <li><svg viewBox="0 0 12 12"><rect x="3" y="1" width="6" height="3" fill="var(--brand-red)"/><rect x="1" y="4.5" width="10" height="4.5" rx="1" fill="var(--brand-red)"/><rect x="3" y="8" width="6" height="3" fill="var(--brand-red)"/></svg>555-310-4821</li>
      <li><svg viewBox="0 0 12 12"><rect x="1" y="2.5" width="10" height="7" fill="none" stroke="var(--brand-red)" stroke-width="1"/><path d="M1 2.5l5 4 5-4" fill="none" stroke="var(--brand-red)" stroke-width="1"/></svg>info@CorvaneSystems.com</li>
      <li><svg viewBox="0 0 12 12"><circle cx="6" cy="6" r="5.3" fill="var(--brand-red)"/><path d="M3 3.5c1.5.3 2 1.5 1.5 2.5s.5 2 1 3M7.5 1.5c-.5 1 .5 2 1.5 2.2s1 1.5.5 2.5" stroke="#fff" stroke-width=".9" fill="none"/></svg>www.CorvaneSystems.com</li>
    </ul>
  </header>

  <section class="letter-body">
    <p class="salutation">Dear customer,</p>
    <p class="copy">Lorem ipsum dolor sit amet, consectetur adipisicing elit, sed do eiusmod tempor incididunt ut labore et dolore magna aliqua. Ut enim ad minim veniam, quis nostrud exercitation ullamco laboris nisi ut aliquip ex ea commodo consequat. Duis aute irure dolor in reprehenderit in voluptate velit esse cillum dolore eu fugiat nulla pariatur. Excepteur sint occaecat cupidatat non proident, sunt in culpa qui officia deserunt mollit anim id est laborum.</p>
    <p class="copy">Lorem ipsum dolor sit amet, consectetur adipisicing elit, sed do eiusmod tempor incididunt ut labore et dolore magna aliqua. Ut enim ad minim veniam, quis nostrud exercitation ullamco laboris nisi ut aliquip ex ea commodo consequat. Duis aute irure dolor in reprehenderit in voluptate velit esse cillum dolore eu fugiat nulla pariatur. Excepteur sint occaecat cupidatat non proident, sunt in culpa qui officia deserunt mollit anim id est laborum.</p>
    <p class="copy">Lorem ipsum dolor sit amet, consectetur adipisicing elit, sed do eiusmod tempor incididunt ut labore et dolore magna aliqua. Ut enim ad minim veniam, quis nostrud exercitation ullamco laboris nisi ut aliquip ex ea commodo consequat. Duis aute irure dolor in reprehenderit in voluptate velit esse cillum dolore eu fugiat nulla pariatur. Excepteur sint occaecat cupidatat non proident, sunt in culpa qui officia deserunt mollit anim id est laborum.</p>
    <p class="copy">Lorem ipsum dolor sit amet, consectetur adipisicing elit, sed do eiusmod tempor incididunt ut labore et dolore magna aliqua. Ut enim ad minim veniam, quis nostrud exercitation ullamco laboris nisi ut aliquip ex ea commodo consequat. Duis aute irure dolor in reprehenderit.</p>
    <p class="closing">Yours Sincerely,</p>
  </section>

  <div class="signature" role="img" aria-label="Handwritten signature"></div>

  <div class="partner-badge" role="img" aria-label="Sustainability programme badge"></div>

  <footer>
    <svg class="footer-wave" viewBox="0 0 747 101" preserveAspectRatio="none" aria-hidden="true">
      <path d="M0 0 Q330 72 747 62 L747 101 L0 101 Z" fill="var(--brand-red)"/>
      <path d="M350 58 Q600 62 747 34 L747 55 Q600 66 350 58 Z" fill="var(--brand-blue)"/>
    </svg>
    <div class="footer-web">
      <svg viewBox="0 0 12 12"><circle cx="6" cy="6" r="5.3" fill="#fff"/><path d="M3 3.5c1.5.3 2 1.5 1.5 2.5s.5 2 1 3M7.5 1.5c-.5 1 .5 2 1.5 2.2s1 1.5.5 2.5" stroke="var(--brand-red)" stroke-width=".9" fill="none"/></svg>
      www.CorvaneSystems.com
    </div>
  </footer>
</main>
</body>
</html>
```